Simple Business Cards for Self-employed Coach

Simple business card with a design that includes the QLT logo.
Using either only the logo color or additional colors that match the logo.

Meridian Guides reach deeply into the past, gathering wisdom from East and West, while still staying current with the frontiers of new discovery in cognitive science, genetics, and other disciplines. see https://www.brightharborpath.example/what-is-integral-coaching/

Target Market(s)

Coaching Clients in Tokyo /Asia; in business organizations, but also outside

Industry/Entity Type

Life Coaching

Contact Information for Business Card

Lukas Brenning
Certified Meridian Guide

3-2-48 Kamiyoshi
Nakarino 164-0392
Tokyo, Japan

Phone: +81 70 4817 5062
E-Mail: lukas.brenning@mailora.example

Font styles to use
Sans Serif

Colors
00a990

Requirements
Must have
• include uploaded logo
• color fitting with QLT logo color
Nice to have
• simple, elegant design
Should not have
• clutter

```html
<!DOCTYPE html>
<html lang="en">
<head>
<meta charset="utf-8">
<title>Lukas Brenning — Business Card</title>
<link rel="stylesheet" href="https://fonts.googleapis.com/css2?family=Arimo:wght@400;700&display=swap">
<style>
  :root {
    --teal: #00a990;
    --teal-bright: #16c2ac;
    --ink: #6b6b6b;
    --card: #ffffff;
    --card-shade: #eeeeee;
    --stage: #e4e2de;
  }
  * { margin: 0; padding: 0; box-sizing: border-box; }
  html, body {
    width: 1200px; height: 1023px; overflow: hidden;
    background: var(--stage);
    font-family: "Arimo", Arial, sans-serif;
  }
  .stage {
    width: 1200px; height: 1023px;
    display: flex; align-items: center; justify-content: center;
  }
  .card {
    position: relative;
    width: 900px; height: 530px;
    border-radius: 26px;
    background: linear-gradient(160deg, var(--card) 55%, var(--card-shade) 100%);
    box-shadow: 0 14px 40px rgba(0,0,0,0.16);
  }
  .brand {
    position: absolute; left: 70px; top: 78px;
    display: flex; align-items: center; gap: 18px;
  }
  .brand-square {
    width: 74px; height: 74px; background: var(--teal);
  }
  .brand-name {
    font-weight: 700; font-size: 64px; letter-spacing: 10px;
    color: var(--teal); line-height: 1;
  }
  .identity {
    position: absolute; right: 70px; top: 92px; text-align: left;
  }
  .person-name {
    font-weight: 700; font-size: 44px; letter-spacing: 1px;
    color: var(--teal-bright); line-height: 1.1;
  }
  .person-title {
    font-size: 22px; color: var(--ink); letter-spacing: 0.5px; margin-top: 6px;
  }
  .contacts {
    list-style: none; margin-top: 36px; display: grid; gap: 14px;
  }
  .contacts li {
    display: flex; align-items: center; gap: 12px;
    font-size: 19px; color: var(--ink); letter-spacing: 1px;
  }
  .contacts svg { width: 18px; height: 18px; flex: none; }
  .address {
    position: absolute; left: 330px; bottom: 60px;
    font-size: 21px; line-height: 1.4; color: var(--ink); letter-spacing: 2px;
    font-style: normal;
  }
</style>
</head>
<body>
<main class="stage">
  <article class="card">
    <div class="brand">
      <span class="brand-square"></span>
      <span class="brand-name">QLT</span>
    </div>

    <section class="identity">
      <h1 class="person-name">Lukas Brenning</h1>
      <p class="person-title">Certified Meridian Guide</p>
      <ul class="contacts">
        <li>
          <svg viewBox="0 0 20 20" aria-hidden="true"><circle cx="10" cy="10" r="9" fill="none" stroke="#00a990" stroke-width="2"/><path d="M7 5.5l2 2-1.2 1.3c.6 1.4 1.6 2.4 3 3l1.3-1.2 2 2-1.4 1.6C9.5 14 6 10.5 5.8 6.8z" fill="#00a990"/></svg>
          +81 70 4817 5062
        </li>
        <li>
          <svg viewBox="0 0 20 20" aria-hidden="true"><rect x="2" y="4.5" width="16" height="11" fill="none" stroke="#00a990" stroke-width="1.8"/><path d="M2 4.5l8 6.5 8-6.5" fill="none" stroke="#00a990" stroke-width="1.8"/></svg>
          lukas.brenning@mailora.example
        </li>
        <li>
          <svg viewBox="0 0 20 20" aria-hidden="true"><circle cx="10" cy="10" r="8.5" fill="none" stroke="#00a990" stroke-width="1.8"/><ellipse cx="10" cy="10" rx="3.6" ry="8.5" fill="none" stroke="#00a990" stroke-width="1.5"/><path d="M1.5 10h17M3 6h14M3 14h14" stroke="#00a990" stroke-width="1.3"/></svg>
          www.brightharborpath.example
        </li>
      </ul>
    </section>

    <address class="address">
      3-2-48 Kamiyoshi<br>
      Nakarino 164-0392<br>
      Tokyo, Japan
    </address>
  </article>
</main>
</body>
</html>
```